Community Bank Web Design

Design a homepage and internal product page for a community bank. Needs to be mobile friendly, minimal scrolling on home. Create the homepage look & feel, then use the same aesthetic to create the product page for the personal checking account page.

Wireframes, logo variations, and color scheme attached.

New brand identity:
• Open, Fresh, Younger, Bright, Bold, New, Innovative.
• Inviting, approachable, friendly, trustworthy.
• Imagine a young family purchasing their first home as the target audience.
You do not have to stick to the exact layout of the wireframes, as long as all of the elements are present.

All navigation elements are specified in wireframes. There are three versions of the homepage – Personal Home, Business Home, Wealth Management Home – you may design whichever version you prefer.

For internal page – please design the Checking product page, included in wireframes.

NOTE: Submit your homepage design first. I will provide feedback on your design direction, then you can use that to move forward with the internal page design.

Design direction--
Some banking / financial sites we like for their fresh/bold/open look:
velmorant.com
quendo.ca
rwxfinancial.org
pvt.co.nz
hopvault.com
pellerbank.com
ulk.co.nz

Target Market(s)

The target market for the personal homepage varies. Adults in the midwest, 25 - 60, who are striving to build their savings and manage their money. Often buying homes or refinancing their homes to make renovations, or planning for retirement.

For the business homepage, the target market are small to mid-market business owners striving to grow their business and manage their company.

Industry/Entity Type

Financial

Requirements
Must have
• colors: CRIMSON #a20c33,
FOREST GREEN #004f38
GOLD #e6a513

File format for design submission must be layered PSD (Please organize layers into recognizable folders like "menu" and "footer")

To make the design "mobile friendly" please create a grid-based layout. http://www.trovask.com/patterns/showPattern.php?patternID=grid-based-layout
http://www.quillbrightjournal.com/2007/04/14/designing-with-grid-based-approach/

```html
<!DOCTYPE html>
<html lang="en">
<head>
<meta charset="utf-8">
<title>Larkmont Valley Bank – Personal Checking Accounts</title>
<link href="https://fonts.googleapis.com/css2?family=Open+Sans:wght@400;600;700&family=Raleway:wght@600;700&display=swap" rel="stylesheet">
<style>
:root{
  --crimson:#a20c33;
  --crimson-soft:#c2365a;
  --forest:#004f38;
  --forest-dark:#033a2a;
  --gold:#e6a513;
  --panel:#f4f4f5;
  --line:#e2e2e4;
  --ink:#333;
  --ink-soft:#555;
  --table-head:#a3a8b2;
  --white:#fff;
}
*{margin:0;padding:0;box-sizing:border-box}
html,body{width:752px;height:1200px;overflow:hidden;background:var(--white)}
body{position:relative;font-family:"Open Sans",Arial,sans-serif;color:var(--ink)}
.abs{position:absolute}
ul{list-style:none}

/* top bar */
.topbar{left:0;top:0;width:752px;height:33px;background:var(--crimson);color:var(--white);font-size:7.5px;font-weight:600;letter-spacing:.2px}
.topbar span{position:absolute;top:12px}
.topbar .sep{opacity:.7}
.topbar .pointer{position:absolute;left:91px;top:28px;width:0;height:0;border-left:5px solid transparent;border-right:5px solid transparent;border-bottom:5px solid var(--white)}
.topbar .util{font-weight:400;font-size:8px;display:flex;align-items:center;gap:4px}
.search{position:absolute;left:562px;top:10px;width:112px;height:15px;border-bottom:1px solid rgba(255,255,255,.7);font-size:8px;font-weight:400}

/* header */
.brand{left:76px;top:58px;display:flex;align-items:center;gap:7px}
.brand-dot{width:34px;height:34px;border-radius:50%;background:var(--crimson)}
.brand-name{font-size:19px;color:var(--crimson);font-weight:400;letter-spacing:-.3px}
.mainnav .item{position:absolute;top:54px;text-align:center;font-size:8px;color:var(--ink-soft);letter-spacing:.3px}
.mainnav .item svg{display:block;margin:0 auto 6px}
.mainnav .item.active{color:var(--forest)}
.mainnav .divider{position:absolute;top:52px;width:1px;height:44px;background:var(--line)}

/* sidebar */
.sidebar{left:71px;top:111px;width:155px;height:861px;background:var(--panel)}
.sidebar h2{height:34px;padding:11px 0 0 14px;font-size:10px;font-weight:700;color:var(--crimson);border-bottom:2px solid var(--crimson);letter-spacing:.2px;background:var(--white)}
.sidebar li{height:28.8px;display:flex;align-items:center;padding-left:14px;font-size:7.2px;border-bottom:1px solid var(--line);color:var(--ink)}
.sidebar li svg{width:12px;margin-right:17px;flex:none}
.sidebar ul{margin-top:7px}
.sidebar li.active{background:var(--forest-dark);color:var(--white)}

/* breadcrumb */
.crumb{left:247px;top:111px;width:434px;height:25px;border:1px solid var(--line);font-size:7px;color:var(--ink-soft);display:flex;align-items:center;padding-left:8px;gap:10px}

/* hero */
.hero{left:247px;top:152px;width:434px;height:192px;background:linear-gradient(100deg,#e9ecf0 0%,#d9dde3 45%,#c9b8aa 70%,#3b4658 100%)}
.hero-title{left:247px;top:171px;width:170px;height:57px;background:var(--crimson-soft);opacity:.95;color:var(--white);font-family:"Raleway",sans-serif;font-weight:600;font-size:14px;line-height:18px;padding:10px 14px}

.intro{left:247px;top:366px;width:274px;font-size:7px;line-height:12.5px;color:var(--ink-soft)}

/* related links */
.related{left:540px;top:368px;width:141px;height:146px;background:var(--panel)}
.related h3{height:26px;background:var(--forest-dark);color:var(--white);font-size:9.5px;font-weight:700;padding:7px 0 0 17px}
.related ul{padding:11px 0 0 17px}
.related li{font-size:7px;height:15.7px;color:var(--ink)}
.related li::before{content:"»";margin-right:9px;font-size:8px}
.related .open{position:absolute;left:0;bottom:0;width:141px;height:21px;background:var(--white);border-bottom:1px solid var(--line);font-size:7.5px;font-weight:700;color:var(--crimson);padding:5px 0 0 17px}

/* compare table */
.compare{left:249px;top:538px;width:432px}
.compare h3{height:28px;background:var(--crimson);color:var(--white);font-size:10px;font-weight:700;padding:7px 0 0 13px;letter-spacing:.2px}
.compare table{width:100%;border-collapse:collapse;font-size:6.8px;color:var(--ink-soft)}
.compare th{height:19px;background:var(--table-head);color:var(--white);font-size:6px;font-weight:700;text-align:center}
.compare td{height:27px;text-align:center}
.compare td:first-child{text-align:left;padding-left:14px;width:45%}
.compare tr:nth-child(odd) td{background:var(--panel)}
.compare tr:last-child td{border-bottom:2px solid var(--line)}

/* tabs */
.tabs{left:249px;top:778px;width:432px;height:33px;display:flex;background:var(--forest-dark)}
.tabs div{display:flex;align-items:center;justify-content:center;font-size:7px;color:var(--white);border-right:1px solid rgba(255,255,255,.25)}
.tabs .current{background:var(--white);color:var(--ink);border-top:1px solid var(--forest-dark)}
.tabpanel{left:249px;top:811px;width:432px;height:161px;background:var(--panel);padding:0 16px 0 18px}
.tabpanel h3{margin-top:17px;font-size:11.5px;font-weight:600;color:var(--ink);letter-spacing:.2px}
.tabpanel p{margin-top:6px;font-size:6.9px;line-height:12.4px;color:var(--ink-soft)}
.btn{display:inline-block;margin-top:12px;width:83px;height:22px;background:var(--gold);color:var(--white);font-size:6.5px;font-weight:600;text-align:center;line-height:22px;letter-spacing:-.2px}

/* footer */
.footer{left:0;top:992px;width:752px;height:166px;background:var(--crimson);color:var(--white)}
.footer .fbrand{position:absolute;left:86px;top:70px;display:flex;align-items:center;gap:6px}
.footer .fbrand .brand-dot{width:26px;height:26px;background:var(--white);opacity:.85}
.footer .fbrand span{font-size:13px;line-height:14px;width:90px}
.footer h4{position:absolute;top:36px;font-size:10px;font-weight:600}
.footer .col{position:absolute;top:57px;font-size:7px;line-height:10.4px}
.footer ul.col li::before{content:"•";margin-right:6px}
.footer .badge{position:absolute;left:538px;top:90px;width:140px;height:32px;background:rgba(255,255,255,.28);border-radius:2px}
.copyright{left:0;top:1172px;width:752px;text-align:center;font-size:6.8px;color:#777}
</style>
</head>
<body>

<header class="topbar abs">
  <span style="left:78px">PERSONAL</span>
  <span class="sep" style="left:124px">|</span>
  <span style="left:132px">BUSINESS</span>
  <span class="sep" style="left:175px">|</span>
  <span style="left:185px">WEALTH &nbsp;MANAGEMENT</span>
  <i class="pointer"></i>
  <span class="util" style="left:354px;top:13px">
    <svg width="8" height="8" viewBox="0 0 10 10"><circle cx="4" cy="4" r="3" fill="none" stroke="#fff" stroke-width="1.5"/><path d="M6.3 6.3 9 9" stroke="#fff" stroke-width="1.6"/></svg>FIND A BRANCH OR ATM</span>
  <span class="util" style="left:478px;top:13px">
    <svg width="6" height="9" viewBox="0 0 6 9"><rect x=".7" y=".7" width="4.6" height="7.6" rx=".8" fill="none" stroke="#fff" stroke-width="1.2"/></svg>CONTACT US</span>
  <div class="search">Search
    <svg style="position:absolute;right:3px;top:1px" width="8" height="8" viewBox="0 0 10 10"><circle cx="4" cy="4" r="3" fill="none" stroke="#fff" stroke-width="1.6"/><path d="M6.3 6.3 9 9" stroke="#fff" stroke-width="1.8"/></svg>
  </div>
</header>

<div class="brand abs"><i class="brand-dot"></i><span class="brand-name">Larkmont Valley Bank</span></div>

<nav class="mainnav">
  <div class="item active" style="left:380px;width:108px">
    <svg width="14" height="13" viewBox="0 0 14 13"><path d="M3.5 1 7 3.2 3.5 5.4 0 3.2zM10.5 1 14 3.2 10.5 5.4 7 3.2zM3.5 5.6 7 7.8 3.5 10 0 7.8zM10.5 5.6 14 7.8 10.5 10 7 7.8zM7 8.4 10 10.4 7 12.4 4 10.4z" fill="#004f38"/></svg>PRODUCT AND SERVICES</div>
  <div class="divider" style="left:502px"></div>
  <div class="item" style="left:512px;width:60px">
    <svg width="9" height="13" viewBox="0 0 9 13"><text x="0" y="11" font-family="Open Sans,sans-serif" font-weight="700" font-size="13" fill="#444">?</text></svg>WHY LVB?</div>
  <div class="divider" style="left:586px"></div>
  <div class="item" style="left:596px;width:86px">
    <svg width="16" height="13" viewBox="0 0 16 13"><circle cx="8" cy="3.5" r="2.6" fill="#444"/><circle cx="3" cy="5" r="2" fill="#444"/><circle cx="13" cy="5" r="2" fill="#444"/><path d="M3.5 12c0-3 2-5 4.5-5s4.5 2 4.5 5zM0 12c0-2 1-3.5 3-3.5 1 0 1.5.3 2 .8-1 .9-1.5 1.6-1.6 2.7zM16 12c0-2-1-3.5-3-3.5-1 0-1.5.3-2 .8 1 .9 1.5 1.6 1.6 2.7z" fill="#444"/></svg>CUSTOMER CENTER</div>
</nav>

<aside class="sidebar abs">
  <h2>PERSONAL</h2>
  <ul>
    <li><svg viewBox="0 0 12 12" height="12"><circle cx="6" cy="3.2" r="2.6" fill="#333"/><path d="M1 12c0-3.5 2.2-5.5 5-5.5s5 2 5 5.5z" fill="#333"/></svg>Checking Accounts</li>
    <li><svg viewBox="0 0 12 10" height="10"><rect x=".6" y=".6" width="10.8" height="8.8" rx="1" fill="none" stroke="#333" stroke-width="1.1"/><path d="M.6 3.5h10.8M2.5 6.5h4" stroke="#333" stroke-width="1.1"/></svg>Debit Cards</li>
    <li class="active"><svg viewBox="0 0 12 12" height="12"><circle cx="7.5" cy="3.5" r="3" fill="#fff"/><path d="M0 8h3l2 1h4l2.5-1.5V9L9 11.5H3L0 10z" fill="#fff"/></svg>Savings &amp; CDs</li>
    <li><svg viewBox="0 0 12 12" height="12"><circle cx="6" cy="4" r="3" fill="none" stroke="#333" stroke-width="1.1"/><path d="M0 9h3l2 1h4l2.5-1.5V10L9 12H3L0 11z" fill="#333"/></svg>Loans</li>
    <li><svg viewBox="0 0 12 10" height="10"><rect x=".6" y=".6" width="10.8" height="8.8" rx="1" fill="none" stroke="#333" stroke-width="1.1"/><path d="M.6 3.5h10.8M2.5 6.5h4" stroke="#333" stroke-width="1.1"/></svg>Credit Cards</li>
    <li><svg viewBox="0 0 12 12" height="12"><circle cx="7.5" cy="3.5" r="3" fill="#333"/><path d="M0 8h3l2 1h4l2.5-1.5V9L9 11.5H3L0 10z" fill="#333"/></svg>Investing</li>
    <li><svg viewBox="0 0 12 12" height="12"><rect x="1" y="1" width="9" height="7" fill="none" stroke="#333" stroke-width="1.1"/><path d="M2 11h7" stroke="#333" stroke-width="1.2"/><circle cx="9.5" cy="9" r="2" fill="#333"/></svg>Online banking</li>
    <li><svg viewBox="0 0 12 12" height="12"><rect x="1" y="1" width="6" height="10" rx="1" fill="none" stroke="#333" stroke-width="1.1"/><circle cx="8.5" cy="4" r="3" fill="#333"/></svg>Mobile banking</li>
    <li><svg viewBox="0 0 12 12" height="12"><circle cx="6" cy="6" r="5" fill="none" stroke="#333" stroke-width="1.1"/><path d="M6 3v6M3 6h6" stroke="#333" stroke-width="1.1"/></svg>Additional services</li>
  </ul>
</aside>

<div class="crumb abs">
  <svg width="9" height="8" viewBox="0 0 9 8"><path d="M4.5 0 9 4H7.6v4H5.5V5.5h-2V8H1.4V4H0z" fill="#004f38"/></svg>
  Product and services
</div>

<div class="hero abs" role="img" aria-label="Photo of a smiling woman and two men shaking hands across a bank desk"></div>
<div class="hero-title abs">Personal Checking Accounts</div>

<p class="intro abs">Lorem ipsum dolor sit amet, consectetur adipiscing elit. Nulla quam velit, vulputate eu pharetra nec, mattis ac neque. Duis vulputate commodo lectus, ac blandit elit tincidunt id. Sed rhoncus, tortor sed eleifend tristique, tortor mauris molestie elit, et lacinia ipsum quam nec dui. Quisque nec mauris sit amet elit iaculis pretium sit amet quis magna. Aenean velit odio, elementum in tempus ut, vehicula eu diam. Pellentesque rhoncus aliquam mattis. Ut vulputate eros sed felis sodales nec vulputate justo hendrerit. Vivamus varius pretium ligula, a aliquam odio euismod sit amet. Quisque laoreet sem sit amet orci ullamcorper at ultricies metus viverra. Pellentesque arcu mauris, malesuada quis ornare accumsan, blandit sed diam.</p>

<section class="related abs">
  <h3>RELATED LINKS</h3>
  <ul>
    <li>Order Checks</li>
    <li>Debit Card</li>
    <li>Overdraft Protection</li>
    <li>Mobile Banking</li>
    <li>Switch Kit</li>
  </ul>
  <div class="open">OPEN CHECKING</div>
</section>

<section class="compare abs">
  <h3>COMPARE CHECKING ACCOUNTS</h3>
  <table>
    <tr><th></th><th>FREE CHECKING</th><th>INTEREST CHECKING</th></tr>
    <tr><td>FREE</td><td><svg width="9" height="9" viewBox="0 0 9 9"><rect x=".5" y=".5" width="8" height="8" rx="1.5" fill="none" stroke="#888"/><path d="M2.2 4.6 3.8 6.2 6.8 2.8" fill="none" stroke="#888"/></svg></td><td><svg width="9" height="9" viewBox="0 0 9 9"><rect x=".5" y=".5" width="8" height="8" rx="1.5" fill="none" stroke="#888"/><path d="M2.2 4.6 3.8 6.2 6.8 2.8" fill="none" stroke="#888"/></svg></td></tr>
    <tr><td>100 of ATMs</td><td><svg width="9" height="9" viewBox="0 0 9 9"><rect x=".5" y=".5" width="8" height="8" rx="1.5" fill="none" stroke="#888"/><path d="M2.2 4.6 3.8 6.2 6.8 2.8" fill="none" stroke="#888"/></svg></td><td><svg width="9" height="9" viewBox="0 0 9 9"><rect x=".5" y=".5" width="8" height="8" rx="1.5" fill="none" stroke="#888"/><path d="M2.2 4.6 3.8 6.2 6.8 2.8" fill="none" stroke="#888"/></svg></td></tr>
    <tr><td>03% INTREST</td><td><svg width="9" height="9" viewBox="0 0 9 9"><rect x=".5" y=".5" width="8" height="8" rx="1.5" fill="none" stroke="#888"/><path d="M2.2 4.6 3.8 6.2 6.8 2.8" fill="none" stroke="#888"/></svg></td><td><svg width="9" height="9" viewBox="0 0 9 9"><rect x=".5" y=".5" width="8" height="8" rx="1.5" fill="none" stroke="#888"/><path d="M2.2 4.6 3.8 6.2 6.8 2.8" fill="none" stroke="#888"/></svg></td></tr>
    <tr><td>MINIMUM TO OPEN</td><td>$100</td><td>$300</td></tr>
    <tr><td>MINIMUM BALANCE REQUIREMENT</td><td>$0</td><td>$300</td></tr>
    <tr><td>MINIMUM TO OPEN</td><td>$100</td><td>$300</td></tr>
  </table>
</section>

<nav class="tabs abs">
  <div style="width:81px">MOBILE BANKING</div>
  <div class="current" style="width:120px">OVER DRAFT PROTECTION</div>
  <div style="width:71px">DEBIT CARD</div>
  <div style="width:86px">DIRECT DEPOSIT</div>
  <div style="width:74px;border-right:0">SWITCH KIT</div>
</nav>
<section class="tabpanel abs">
  <h3>OVER DRAFT PROTECTION</h3>
  <p>Lorem ipsum dolor sit amet, consectetur adipiscing elit. Nulla quam velit, vulputate eu pharetra nec, mattis ac neque. Duis vulputate commodo lectus, ac blandit elit tincidunt id. Sed rhoncus, tortor sed eleifend tristique, tortor mauris molestie elit, et lacinia ipsum quam nec dui. Quisque nec mauris sit amet elit iaculis pretium sit amet quis magna. Aenean velit odio, elementum in tempus ut, vehicula eu diam. Pellentesque rhoncus aliquam mattis. Ut vulputate eros sed felis sodales nec vulputate justo hendrerit.</p>
  <span class="btn">OPT IN TODAY!</span>
</section>

<footer class="footer abs">
  <div class="fbrand"><i class="brand-dot"></i><span>Larkmont Valley Bank</span></div>
  <h4 style="left:240px">About Us</h4>
  <p class="col" style="left:238px;width:124px">Lorem ipsum dolor sit amet, consectetur adipiscing elit. Nulla quam velit, vulputate eu pharetra nec, mattis ac neque. Duis vulputate commodo lectus, ac blandit elit tincidunt id. Sed rhonc</p>
  <h4 style="left:406px">More information</h4>
  <ul class="col" style="left:406px">
    <li>Privacy Policy</li><li>Careers</li><li>CRA</li><li>Member DICA</li><li>Contrary to popular</li><li>Lorem Ipsum passage</li>
  </ul>
  <h4 style="left:538px">Investor Relations Link</h4>
  <ul class="col" style="left:538px">
    <li>Contrary to popular</li><li>Lorem Ipsum passage</li>
  </ul>
  <div class="badge"></div>
</footer>
<p class="copyright abs">2014© Larkmont Valley Bank allright Reserved</p>

</body>
</html>
```